Zielgruppe
wir sind eine Sicherheitsunternehmen und suchen ein ausgefallenes Design um alle Privathaushalte sowohl auch kleine und große Firmen zu beindrucken.
Aufgabenstellung
Die Firma möchte das erste Sicherheitsunternehmen sein was absolut Nachhaltig, ökologisch und umweltfreundlich arbeitet. Die Natur, der Klimawechsel steht im absoluten Vordergrund. Wir möchten zeigen das man auch als Dienstleister im Sicheheitsbereich im Einklang mit der Umwelt sein kann. und mit diesem Konzept möchten wir an die Bevölkerung rantreten. Das Motto: mit uns als Partner werden Fremdfirmen mehr Kunden gewinnen, da wir umweltbewusst und mit den uns verfügbaren Ressourcen sehr ökologisch und grün sind. Das Design sollte bitte nicht in schrillen Farben dargestellt werden. Das Logo und unsere Grundfarben sind Schwarz/ Antrazith/ Weiss/Creme und Naturrholzfarben.

```html
<!DOCTYPE html>
<html lang="de">
<head>
<meta charset="utf-8">
<title>Lumen Sicherheit – Faltblatt</title>
<link href="https://fonts.googleapis.com/css2?family=Arimo:wght@400;700&display=swap" rel="stylesheet">
<style>
  :root{
    --page:#ffffff;
    --sky:#d3e0f3;
    --ink:#1f1f1f;
    --navy-top:#0a1a36;
    --navy-mid:#163059;
    --navy-low:#0c1f3d;
    --cream:#efe2c2;
    --ice:#dfe9f7;
    --steel:#9a9ea6;
    --olive:#8a8a22;
    --meadow:#a9b83a;
    --sun:#e9d772;
  }
  *{margin:0;padding:0;box-sizing:border-box}
  html,body{width:1200px;height:572px;overflow:hidden;background:var(--page)}
  body{position:relative;font-family:"Arimo",Arial,sans-serif;color:var(--ink)}
  .panel{position:absolute;top:0;height:572px;overflow:hidden}
  .panel-front{left:8px;width:285px;background:linear-gradient(180deg,#f3f1e4 50%,#c9c46a 80%,#9bb03a 100%)}
  .panel-inside{left:316px;width:571px;background:radial-gradient(ellipse at 72% 30%,var(--navy-mid) 0%,var(--navy-top) 55%,var(--navy-low) 100%)}
  .panel-back{left:913px;width:285px;background:linear-gradient(180deg,#fbfbf6 0%,#f2f1d8 30%,var(--sun) 52%,var(--olive) 75%,#5f6a1c 100%)}

  .sky-band{position:absolute;left:0;top:0;width:100%;height:147px;background:var(--sky)}
  .front-headline{position:absolute;left:0;top:16px;width:100%;text-align:center;font-weight:700;font-size:23.5px;line-height:30.5px}
  .front-values{position:absolute;left:0;top:104px;width:100%;text-align:center;font-size:18px;line-height:23px}
  .globe-photo{position:absolute;left:0;top:170px;width:100%;height:270px;
    background:radial-gradient(circle at 50% 42%,#2e5f9c 0%,#3c6e8c 28%,#c7b79d 50%,rgba(233,214,150,0) 75%)}
  .front-name{position:absolute;left:0;top:416px;width:100%;text-align:center;color:#fff;font-weight:700;font-size:9px;letter-spacing:1.1px;text-transform:uppercase}
  .photo-strip{position:absolute;left:0;top:440px;width:100%;height:80px;display:flex}
  .photo-strip span{flex:1;height:100%}
  .strip-family{background:linear-gradient(135deg,#b08f6a,#d9c2a2)}
  .strip-seniors{background:linear-gradient(135deg,#d8cfc2,#8a6d4e)}
  .strip-workshop{background:linear-gradient(135deg,#6d7c90,#2f4b7a)}
  .strip-factory{background:linear-gradient(135deg,#b69a5c,#6f6650);flex:1.45!important}
  .front-slogan{position:absolute;left:0;top:526px;width:100%;text-align:center;color:#fff;font-weight:700;font-size:14.5px}

  .guard-photo{position:absolute;left:330px;top:40px;width:230px;height:520px;
    background:radial-gradient(ellipse at 45% 40%,rgba(40,70,120,.55) 0%,rgba(10,26,54,0) 70%)}
  .torch-glow{position:absolute;left:400px;top:80px;width:36px;height:36px;border-radius:50%;
    background:radial-gradient(circle,#ffffff 0%,#e6f0ff 40%,rgba(120,160,230,0) 75%)}
  .col{position:absolute;text-align:center}
  .col-mission{left:32px;width:250px;top:33px;color:#fff}
  .col-services{left:320px;width:240px;top:33px;color:#fff}
  .cream-head{color:var(--cream);font-weight:700;font-size:16px;line-height:19.3px}
  .body-text{font-size:13px;line-height:15.4px}
  .sub-head{font-weight:700;font-size:13px;line-height:15.4px;margin-top:18px}
  .spacer{height:15px}
  .services-title{color:var(--cream);font-weight:700;font-size:15px;margin-top:41px;line-height:17px}
  .service{font-size:12.3px;line-height:13.5px;color:var(--ice);margin-top:5px}
  .service b{font-size:13px;color:#eef3fb}
  .service:first-of-type{margin-top:1px}
  .services-note{font-size:12.6px;line-height:15.3px;margin-top:6px}
  .services-claim{color:var(--cream);font-weight:700;font-size:15px;line-height:15.5px;margin-top:8px}
  .inside-name{position:absolute;left:0;top:526px;width:100%;text-align:center;color:var(--steel);font-weight:700;font-size:12px;letter-spacing:2px;text-transform:uppercase}

  .back-text{position:absolute;left:12px;width:261px;top:20px;text-align:center}
  .back-head{font-weight:700;font-size:15px;line-height:18px;margin-bottom:3px}
  .back-head+.back-head{margin-top:3px}
  .back-body{font-size:13px;line-height:15.4px;margin-top:8px}
  .back-call{font-weight:700;font-size:15px;line-height:19px;margin-top:6px;color:#2a2a14}
  .back-sign{position:absolute;left:0;top:498px;width:100%;text-align:center}
  .back-name{font-weight:700;font-size:9px;letter-spacing:1.1px;text-transform:uppercase;color:#111;margin-bottom:6px}
  .back-contact{font-size:9.5px;line-height:11.6px;color:#fff}
</style>
</head>
<body>

<section class="panel panel-front">
  <div class="sky-band"></div>
  <h1 class="front-headline">Wenn es darauf<br>ankommt, bewachen<br>wir die ganze Welt...</h1>
  <p class="front-values">...ökologisch<br>nachhaltig<br>umweltfreundlich</p>
  <div class="globe-photo" role="img" aria-label="Foto: Erdkugel liegt auf einer offenen Hand vor Sonnenlicht und Wiese"></div>
  <div class="front-name">Lumen Sicherheit Mirabell Huter</div>
  <div class="photo-strip">
    <span class="strip-family" role="img" aria-label="Foto: Familie mit Kindern"></span>
    <span class="strip-seniors" role="img" aria-label="Foto: älteres Ehepaar"></span>
    <span class="strip-workshop" role="img" aria-label="Foto: Kfz-Werkstatt mit Hebebühne"></span>
    <span class="strip-factory" role="img" aria-label="Foto: Werkshalle mit Maschinen"></span>
  </div>
  <p class="front-slogan">Sicherheit, die sich jeder leisten kann</p>
</section>

<section class="panel panel-inside">
  <div class="guard-photo" role="img" aria-label="Foto: Sicherheitsmitarbeiter mit Taschenlampe bei Nacht"></div>
  <div class="torch-glow"></div>

  <div class="col col-mission">
    <h2 class="cream-head">Wir sind eins der ersten Sicherheitsunternehmen, die nachhaltig, ökologisch und umweltfreundlich arbeiten.</h2>
    <p class="sub-head">Was heißt das?</p>
    <p class="body-text">Wir sind ein zu 95% ökologischer Betrieb. Unsere Dienstfahrzeuge sind ausschließlich Hybridfahrzeuge. Die Dientskleidung wird so weit wie möglich ökologisch und ohne Kinder&shy;arbeit hergestellt. Unsere Betriebs&shy;räume werden mit 100%-Ökostrom betrieben. Inneneinrichtungen sowie Büromaterial sind aus recyclebaren Rohstoffen.</p>
    <div class="spacer"></div>
    <p class="body-text">Sicherheit heißt frei von Angst und Gefahr zu sein. Mit steigender Kri&shy;minalität steigt das Bedürfniss nach Sicherheit. Wir bieten alle erfoder&shy;lichen Voraussetzungen zur Siche&shy;rung von Personen, Gebäuden, Einrichtungen und Sachwerten.<br>Dazu übernehmen wir aber<br>auch Urlaubsvertretungen<br>wie Versorgung von<br>Tieren oder<br>Pflanzen.</p>
  </div>

  <div class="col col-services">
    <h2 class="cream-head" style="font-size:15.5px;line-height:17.5px">Sicherheit für Familien, Klein&shy;betriebe, Firmen, Groß&shy;objekte, Veranstaltungen usw.</h2>
    <h3 class="services-title">Das sind unsere Leistungen:</h3>
    <p class="service"><b>Objektschutz</b> wie z.B.<br>Gebäudebewachung<br>Bühnenbewachung<br>Baustellenbewachung<br>Revierkontrollen<br>Außenkontrollen</p>
    <p class="service"><b>Werkschutz</b><br>Pfortendienste<br>Nachtdienste</p>
    <p class="service"><b>Veranstaltungsschutz</b></p>
    <p class="service"><b>Sicherheitstransporte</b><br>Dokumentenlieferung<br>Werttransporte</p>
    <p class="service"><b>Zugbegleitung</b><br>Fahrausweiskontrolle</p>
    <p class="service"><b>Personenschutz</b></p>
    <p class="services-note">Die Palette ist so groß, dass wir nur einen kleinen Teil aufzählen können. fragen Sie danach.</p>
    <p class="services-claim">Mit unserer Leistung<br>gewinnen Sie<br>neue Kunden!</p>
  </div>

  <div class="inside-name">Lumen Sicherheit Mirabell Huter</div>
</section>

<section class="panel panel-back">
  <div class="back-text">
    <h2 class="back-head">Sie wollen mehr über uns erfahren?</h2>
    <h2 class="back-head">Sie haben Fragen?</h2>
    <h2 class="back-head">Sie benötigen Beratung?</h2>
    <p class="back-body">Für alle Ihre Fragen nehmen wir uns viel Zeit. Gern laden wir Sie zu ausführli&shy;chen und kostenfreien Informations- und Beratungsgesprächen ein. Unser kompetentes, intensiv geschultes Team steht Ihnen jederzeit zur Verfügung.</p>
    <p class="back-body">Wir sind Mitglied im Verband Wachdienste und der Schutzgenossenschaft, sowie Fördermitglied der Tierschutzinitiative Nord.</p>
    <p class="back-body">Demnächst bieten wir in unseren Räumen diverse Schulungen wie Ersthelfer, Brandschutz usw. an. Mehr darüber dann auf unserer Internetseite.</p>
    <p class="back-call">Vereinbaren Sie mit uns unter 04412-8731099 einen Termin</p>
  </div>
  <div class="back-sign">
    <div class="back-name">Lumen Sicherheit Mirabell Huter</div>
    <p class="back-contact">Lumen Sicherheit Mirabell Huter<br>Wachtweg 7 - 12345 Grünfelden<br>04412-87310 - Mobil 0157-902614<br>info@lumen-schutz.de - www.lumen-schutz.de</p>
  </div>
</section>

</body>
</html>
```